New Webpage for High Class Expert Witness Services Company

We are looking for a minimalist design for a webpage that just has our logo and an entry form offer to connect with one of our Liaisons.
The entry form should just ask for Name, Email, Contact Info and Description of Project.

Company Name is: The Marlowe Crest Defense Services

Number of Pages Required

1 page

```html
<!DOCTYPE html>
<html lang="en">
<head>
<meta charset="utf-8">
<title>The Marlowe Crest Defense Services — Connect with a Liaison</title>
<link rel="stylesheet" href="https://fonts.googleapis.com/css2?family=Schibsted+Grotesk:wght@400;500&display=swap">
<style>
  :root {
    --page-bg: #121212;
    --card-top: #dcdbd8;
    --card-mid: #f8f8f6;
    --card-bottom: #ebebea;
    --field-border: #8a8a8a;
    --label: #161616;
    --placeholder: #8c8c8c;
    --button-bg: #141414;
    --button-text: #ffffff;
    --footer-text: #f2f2f2;
    --brand-text: #e6e6e6;
  }
  * { box-sizing: border-box; margin: 0; padding: 0; }
  html, body {
    width: 1200px; height: 732px; overflow: hidden;
    background: var(--page-bg);
    font-family: "Schibsted Grotesk", Arial, sans-serif;
  }
  .page { position: relative; width: 1200px; height: 732px; }

  .brand {
    position: absolute; top: 48px; left: 0; width: 1200px;
    display: flex; justify-content: center; align-items: center; gap: 12px;
  }
  .brand-mark { width: 14px; height: 14px; background: var(--brand-text); }
  .brand-name {
    color: var(--brand-text); font-size: 22px; font-weight: 500;
    letter-spacing: 0.06em; text-transform: uppercase;
  }

  .contact-card {
    position: absolute; left: 176px; top: 139px; width: 849px; height: 525px;
    border-radius: 32px;
    background: linear-gradient(180deg, var(--card-top) 0%, var(--card-mid) 50%, var(--card-bottom) 100%);
  }
  .field { position: absolute; }
  .field-label {
    position: absolute; left: 29px; top: -27px;
    font-size: 14px; color: var(--label); white-space: nowrap;
  }
  .field-input {
    width: 100%; height: 100%;
    border: 1px solid var(--field-border); border-radius: 24px;
    background: transparent;
    padding: 0 29px; font: 400 11.5px "Schibsted Grotesk", Arial, sans-serif;
    color: var(--label); outline: none; appearance: none;
  }
  .field-input::placeholder { color: var(--placeholder); }
  textarea.field-input { border-radius: 28px; padding: 18px 29px; resize: none; }
  .field-select { display: flex; align-items: center; justify-content: space-between; color: var(--placeholder); }
  .select-caret { width: 10px; height: 9px; }

  .send-button {
    position: absolute; left: 285px; top: 433px; width: 290px; height: 47px;
    border: none; border-radius: 24px;
    background: var(--button-bg); color: var(--button-text);
    font: 400 15px "Schibsted Grotesk", Arial, sans-serif; letter-spacing: 0.02em;
  }

  .site-footer {
    position: absolute; top: 688px; left: 0; width: 1200px; text-align: center;
    color: var(--footer-text); font-size: 11.5px;
  }
</style>
</head>
<body>
<div class="page">
  <header class="brand">
    <span class="brand-mark"></span>
    <span class="brand-name">The Marlowe Crest Defense Services</span>
  </header>

  <form class="contact-card">
    <div class="field" style="left:51px; top:68px; width:368px; height:48px;">
      <label class="field-label">Name</label>
      <input class="field-input" type="text" placeholder="Enter your name...">
    </div>
    <div class="field" style="left:430px; top:68px; width:368px; height:48px;">
      <label class="field-label">Email</label>
      <input class="field-input" type="email" placeholder="Enter your email...">
    </div>
    <div class="field" style="left:51px; top:160px; width:368px; height:48px;">
      <label class="field-label">Phone Number</label>
      <input class="field-input" type="tel" placeholder="Enter your phone number...">
    </div>
    <div class="field" style="left:430px; top:160px; width:368px; height:48px;">
      <label class="field-label">Country</label>
      <div class="field-input field-select">
        <span>Select</span>
        <svg class="select-caret" viewBox="0 0 10 9"><path d="M0 0h10L5 9z" fill="#111"/></svg>
      </div>
    </div>
    <div class="field" style="left:51px; top:256px; width:748px; height:149px;">
      <label class="field-label">Porject</label>
      <textarea class="field-input" placeholder="Project Description..."></textarea>
    </div>
    <button class="send-button" type="button">SEND</button>
  </form>

  <footer class="site-footer">© Copyright 2026 | The Marlowe Crest Defense Services | All Right Reserved</footer>
</div>
</body>
</html>
```